TideWillowNook.com needs updated website design.

TideWillowNook.com offers individuals a quick, hassle-free way of selling their car, rv, or boat in the Sun City Center, FL area. We will come to the customer's place of choosing in order to give them an in-person offer for their car, rv, or boat. Looking for a website design that will allow users to input their vehicle details as well as their contact info in order to schedule a time and place for our staff to come make them an offer. Currently have an active site that can be referenced.

Target Market(s)

Older people who no longer need their cars.

Industry/Entity Type

Automotive

Coding

Coded - Design and coding required

Number of Pages Required

3 page

Font styles to use
Sans Serif

Colors
a1cd3a
33b8a4

Requirements
Must have
• Trustworthy theme, Emphasis on capturing contact info (contact form visible at all times). Standard privacy policy. Wordpress theme

```html
<!DOCTYPE html>
<html lang="en">
<head>
<meta charset="utf-8">
<title>TideWillowNook.com</title>
<link href="https://fonts.googleapis.com/css2?family=Poppins:wght@300;400;500;600;700&family=Courgette&display=swap" rel="stylesheet">
<style>
:root{
  --teal:#33b8a4;
  --green:#a1cd3a;
  --ink:#1e1e1e;
  --muted:#555;
  --field:#f2f2f2;
  --soft:#f3f3f3;
  --white:#fff;
}
*{box-sizing:border-box;margin:0;padding:0}
html,body{width:1200px;height:2803px;overflow:hidden}
body{font-family:'Poppins',sans-serif;color:var(--ink);background:var(--white);position:relative}
.abs{position:absolute}
a{color:inherit;text-decoration:none}

/* header */
.site-header{position:absolute;left:0;top:0;width:1200px;height:91px;background:var(--white)}
.brand{position:absolute;left:133px;top:26px;display:flex;align-items:center}
.brand-name{font-weight:600;font-size:22px;color:#333;line-height:28px}
.header-phone{left:778px;top:20px;font-size:13px;font-weight:500;display:flex;align-items:center;gap:10px}
.quote-btn{left:910px;top:14px;width:156px;height:27px;background:var(--teal);color:#fff;font-size:12.5px;display:flex;align-items:center;justify-content:center}
.main-nav{left:483px;top:57px;display:flex;gap:26px;font-size:13px;font-weight:500}
.main-nav a.active{color:var(--teal)}

/* hero */
.hero{left:0;top:91px;width:1200px;height:526px;background:linear-gradient(90deg,#4a4a4a,#8a8a8a 45%,#b5b5b5 70%,#6a6a6a)}
.hero-title{left:0;top:268px;width:1200px;text-align:center;color:#fff}
.hero-title .lead{font-size:32px;font-weight:500;line-height:40px;opacity:.92}
.hero-title .big{font-size:46px;font-weight:700;line-height:56px}

.quick-contact{left:133px;top:543px;width:934px;height:145px;background:#fff;box-shadow:0 3px 14px rgba(0,0,0,.15)}
.quick-contact h3{position:absolute;left:27px;top:13px;font-size:15.5px;font-weight:500}
.field{position:absolute;background:var(--field);font-size:11.5px;color:#777;padding:9px 14px}
.submit-btn{position:absolute;left:778px;top:46px;width:117px;height:80px;background:var(--teal);color:#fff;font-weight:600;font-size:13.5px;display:flex;align-items:center;justify-content:center}

.offer{left:0;top:736px;width:1200px;text-align:center}
.offer h2{font-size:21px;font-weight:500;line-height:30px}
.offer p{font-size:18px;line-height:28px}

/* features */
.features{left:0;top:828px;width:1200px;height:169px;display:flex;gap:2px;background:#ddd}
.feature{flex:1;position:relative;background:linear-gradient(135deg,#5e5850,#2f2e2d)}
.feature .script{position:absolute;left:19px;top:105px;font-family:'Courgette',cursive;font-size:24px;color:var(--green)}
.feature .line{position:absolute;left:19px;top:135px;font-size:14px;color:#fff;font-weight:500}

/* showcase */
.showcase{left:0;top:997px;width:1200px;height:536px;background:var(--teal)}
.section-title{position:absolute;left:0;width:1200px;text-align:center;font-size:28px;font-weight:600}
.view-all{position:absolute;font-size:13px;display:flex;align-items:center;gap:8px}
.car-card{position:absolute;top:116px;width:218px;color:#fff}
.car-photo{height:155px}
.car-name{margin-top:16px;font-size:14.5px}
.spec{display:flex;align-items:center;justify-content:space-between;font-size:13px;height:36px;border-bottom:1px solid rgba(255,255,255,.35);padding-right:8px}
.spec span{display:flex;align-items:center;gap:8px}
.car-price{margin-top:13px;font-size:18.5px;font-weight:500}
.car-btn{margin-top:12px;height:34px;border:1px solid #fff;display:flex;align-items:center;justify-content:center;font-size:13px}
.car-btn.solid{background:#fff;color:var(--ink)}

/* about */
.about-frame{left:133px;top:1658px;width:457px;height:310px;background:var(--soft)}
.about-photo{left:168px;top:1602px;width:387px;height:331px;background:linear-gradient(135deg,#e7e4dd,#8a8f96 55%,#3d4a66)}
.years-badge{left:475px;top:1853px;width:80px;height:80px;background:var(--green);color:#fff;text-align:center}
.years-badge b{display:block;font-size:38px;font-weight:600;line-height:44px;margin-top:4px}
.years-badge span{font-size:17px;line-height:20px}
.about-text{left:669px;top:1592px;width:405px}
.about-text h2{font-size:28px;font-weight:600;line-height:40px;margin-bottom:20px}
.about-text p{font-size:12.5px;line-height:19.5px}
.about-list{list-style:none;margin-top:14px}
.about-list li{font-size:12.2px;line-height:19.5px;padding-left:22px;position:relative;margin-bottom:26px}
.about-list li svg{position:absolute;left:0;top:4px}
.read-btn{left:669px;top:1929px;width:104px;height:32px;background:var(--teal);color:#fff;font-size:13px;display:flex;align-items:center;justify-content:center}

/* blogs */
.blogs{left:0;top:2038px;width:1200px;height:447px;background:var(--soft)}
.blog-card{position:absolute;top:123px;width:298px}
.blog-photo{height:176px}
.blog-date{margin-top:21px;font-size:12px;font-weight:500}
.blog-excerpt{margin-top:9px;font-size:12.5px;line-height:18px;color:var(--muted)}
.blog-more{margin-top:9px;font-size:12px;color:var(--teal)}
.blog-more.dark{color:var(--ink)}

/* footer */
.site-footer{left:0;top:2485px;width:1200px;height:318px;background:#fff}
.footer-brand{left:0;top:60px;width:1200px;text-align:center}
.contact-bar{left:170px;top:132px;width:860px;height:89px;background:#fff;box-shadow:0 2px 14px rgba(0,0,0,.08)}
.cb-item{position:absolute;font-size:13px;line-height:19px}
.socials{position:absolute;left:708px;top:32px;display:flex;gap:18px}
.socials i{display:block;width:20px;height:20px;background:#8a8f96;border-radius:3px}
.footer-nav{left:0;top:248px;width:1200px;display:flex;justify-content:center;gap:29px;font-size:12.5px}
.footer-nav a.active{color:var(--teal)}
.copyright{left:0;top:2773px;width:1200px;text-align:center;font-size:11.5px;color:#999}
</style>
</head>
<body>

<header class="site-header">
  <div class="brand"><div class="brand-name">TideWillowNook.com</div></div>
  <div class="abs header-phone">
    <svg width="14" height="14" viewBox="0 0 24 24"><path fill="#33b8a4" d="M6.6 10.8a15 15 0 0 0 6.6 6.6l2.2-2.2a1 1 0 0 1 1-.25 11.4 11.4 0 0 0 3.6.57 1 1 0 0 1 1 1V20a1 1 0 0 1-1 1A17 17 0 0 1 3 4a1 1 0 0 1 1-1h3.5a1 1 0 0 1 1 1c0 1.25.2 2.45.57 3.57a1 1 0 0 1-.25 1z"/></svg>
    555-014-2788
  </div>
  <a class="abs quote-btn" href="#">Online Quote Request</a>
  <nav class="abs main-nav">
    <a class="active" href="#">Home</a><a href="#">Car for Sale</a><a href="#">Rv for Sale</a><a href="#">Boats Sale</a><a href="#">How it Works</a><a href="#">Blogs</a><a href="#">Conatct Us</a>
  </nav>
</header>

<section class="abs hero" role="img" aria-label="Hand holding car keys, hand offering cash, silver car in background"></section>
<div class="abs hero-title">
  <div class="lead">We Don't Sell Cars</div>
  <div class="big">We Sell A Dream</div>
</div>

<form class="abs quick-contact">
  <h3>Quick Contact</h3>
  <div class="field" style="left:27px;top:46px;width:216px;height:32px">Name</div>
  <div class="field" style="left:263px;top:46px;width:216px;height:32px">Email</div>
  <div class="field" style="left:27px;top:93px;width:216px;height:32px">Phone</div>
  <div class="field" style="left:263px;top:93px;width:216px;height:32px">What are you looking for?</div>
  <div class="field" style="left:499px;top:46px;width:258px;height:80px">Message</div>
  <div class="submit-btn">SUBMIT</div>
</form>

<div class="abs offer">
  <h2>Get Your Free In Person Cash Offer Today</h2>
  <p>“Don't Sell Til You Give Me A Yell”</p>
</div>

<section class="abs features">
  <div class="feature" role="img" aria-label="Happy man hugging his car"><div class="script">Fast</div><div class="line">I'll Be at Your Door Today</div></div>
  <div class="feature" role="img" aria-label="Couple in car receiving keys"><div class="script">Fair</div><div class="line">Get Fair Price for Your Vehicle</div></div>
  <div class="feature" role="img" aria-label="Dealer shaking hands with customer"><div class="script">Friendly</div><div class="line">Trusted for Over 25 Years</div></div>
  <div class="feature" role="img" aria-label="Customers signing paperwork"><div class="script">Hassle Free</div><div class="line">I Handle All the Paperwork</div></div>
</section>

<section class="abs showcase">
  <h2 class="section-title" style="top:44px">Our Showcase</h2>
  <a class="view-all" style="left:999px;top:64px;color:#fff" href="#">View All
    <svg width="12" height="10" viewBox="0 0 12 10"><path d="M0 5h10M6 1l4 4-4 4" stroke="#fff" stroke-width="1.6" fill="none"/></svg></a>

  <div class="car-card" style="left:133px">
    <div class="car-photo" role="img" aria-label="Blue hatchback car by the sea" style="background:linear-gradient(160deg,#9fb8c4,#1b9bc0 55%,#445)"></div>
    <div class="car-name">2020 Model Name</div>
    <div class="spec"><span><svg width="14" height="14" viewBox="0 0 14 14"><rect x="1" y="2.5" width="12" height="10.5" fill="none" stroke="#fff" stroke-width="1.4"/><path d="M1 5.5h12M4 1v3M10 1v3" stroke="#fff" stroke-width="1.4"/></svg>Years</span>2020</div>
    <div class="spec"><span><svg width="14" height="14" viewBox="0 0 14 14"><circle cx="7" cy="7" r="5.8" fill="none" stroke="#fff" stroke-width="1.4"/><path d="M7 7l3-3" stroke="#fff" stroke-width="1.4"/></svg>Kilometers</span>3,800</div>
    <div class="car-price">$26,990</div>
    <div class="car-btn">View Details</div>
  </div>
  <div class="car-card" style="left:372px">
    <div class="car-photo" role="img" aria-label="White motor yacht on green water" style="background:linear-gradient(160deg,#2d6f63,#e6ece9 50%,#1f6e66)"></div>
    <div class="car-name">2020 Model Name</div>
    <div class="spec"><span><svg width="14" height="14" viewBox="0 0 14 14"><rect x="1" y="2.5" width="12" height="10.5" fill="none" stroke="#fff" stroke-width="1.4"/><path d="M1 5.5h12M4 1v3M10 1v3" stroke="#fff" stroke-width="1.4"/></svg>Years</span>2020</div>
    <div class="spec"><span><svg width="14" height="14" viewBox="0 0 14 14"><circle cx="7" cy="7" r="5.8" fill="none" stroke="#fff" stroke-width="1.4"/><path d="M7 7l3-3" stroke="#fff" stroke-width="1.4"/></svg>Kilometers</span>3,800</div>
    <div class="car-price">$26,990</div>
    <div class="car-btn solid">View Details</div>
  </div>
  <div class="car-card" style="left:610px">
    <div class="car-photo" role="img" aria-label="White motorhome RV parked" style="background:linear-gradient(160deg,#e9eef2,#c8ccd0 60%,#6f7378)"></div>
    <div class="car-name">2020 Model Name</div>
    <div class="spec"><span><svg width="14" height="14" viewBox="0 0 14 14"><rect x="1" y="2.5" width="12" height="10.5" fill="none" stroke="#fff" stroke-width="1.4"/><path d="M1 5.5h12M4 1v3M10 1v3" stroke="#fff" stroke-width="1.4"/></svg>Years</span>2020</div>
    <div class="spec"><span><svg width="14" height="14" viewBox="0 0 14 14"><circle cx="7" cy="7" r="5.8" fill="none" stroke="#fff" stroke-width="1.4"/><path d="M7 7l3-3" stroke="#fff" stroke-width="1.4"/></svg>Kilometers</span>3,800</div>
    <div class="car-price">$26,990</div>
    <div class="car-btn">View Details</div>
  </div>
  <div class="car-card" style="left:849px">
    <div class="car-photo" role="img" aria-label="Black SUV in a car lot" style="background:linear-gradient(160deg,#b9c3cf,#3a3b3f 55%,#7b7f85)"></div>
    <div class="car-name">2020 Model Name</div>
    <div class="spec"><span><svg width="14" height="14" viewBox="0 0 14 14"><rect x="1" y="2.5" width="12" height="10.5" fill="none" stroke="#fff" stroke-width="1.4"/><path d="M1 5.5h12M4 1v3M10 1v3" stroke="#fff" stroke-width="1.4"/></svg>Years</span>2020</div>
    <div class="spec"><span><svg width="14" height="14" viewBox="0 0 14 14"><circle cx="7" cy="7" r="5.8" fill="none" stroke="#fff" stroke-width="1.4"/><path d="M7 7l3-3" stroke="#fff" stroke-width="1.4"/></svg>Kilometers</span>3,800</div>
    <div class="car-price">$26,990</div>
    <div class="car-btn">View Details</div>
  </div>
</section>

<div class="abs about-frame"></div>
<div class="abs about-photo" role="img" aria-label="Man in suit holding a toy car and documents"></div>
<div class="abs years-badge"><b>25</b><span>Years</span></div>
<div class="abs about-text">
  <h2>About Us</h2>
  <p>We offer the most convenient way of selling your vehicle. We will come to you at a place of your choosing, i.e. home, office, or any other public place.&nbsp; We will give you an in person cash offer on the spot.</p>
  <ul class="about-list">
    <li><svg width="12" height="12" viewBox="0 0 12 12"><circle cx="6" cy="6" r="6" fill="#333"/><path d="M5 3.5 7.5 6 5 8.5" stroke="#fff" stroke-width="1.4" fill="none"/></svg>Got an old clunker? I'll But It! – Turn it into cash today!</li>
    <li><svg width="12" height="12" viewBox="0 0 12 12"><circle cx="6" cy="6" r="6" fill="#333"/><path d="M5 3.5 7.5 6 5 8.5" stroke="#fff" stroke-width="1.4" fill="none"/></svg>Got a nice car you just don't need? I'll Buy It! – Stop wasting money on insurance, registration and maintenance costs!</li>
    <li><svg width="12" height="12" viewBox="0 0 12 12"><circle cx="6" cy="6" r="6" fill="#333"/><path d="M5 3.5 7.5 6 5 8.5" stroke="#fff" stroke-width="1.4" fill="none"/></svg>Got a car that needs repairs? I'll Buy It! – No matter what the issue is I'll come take it away today!</li>
  </ul>
</div>
<a class="abs read-btn" href="#">Read More</a>

<section class="abs blogs">
  <h2 class="section-title" style="top:48px">Blogs</h2>
  <a class="view-all" style="left:1003px;top:68px;color:#666" href="#">View All
    <svg width="12" height="10" viewBox="0 0 12 10"><path d="M0 5h10M6 1l4 4-4 4" stroke="#666" stroke-width="1.6" fill="none"/></svg></a>
  <article class="blog-card" style="left:133px">
    <div class="blog-photo" role="img" aria-label="Couple looking at a new car in showroom" style="background:linear-gradient(135deg,#c9d3dc,#7f8fa3 60%,#3b4656)"></div>
    <div class="blog-date">17/01/2020</div>
    <p class="blog-excerpt">Lorem Ipsum is simply dummy text of the printing and typesetting industry.</p>
    <div class="blog-more">Read More...</div>
  </article>
  <article class="blog-card" style="left:451px">
    <div class="blog-photo" role="img" aria-label="Salesman discussing documents with couple" style="background:linear-gradient(135deg,#3d5f86,#d9dde3 55%,#e3c6b4)"></div>
    <div class="blog-date">17/01/2020</div>
    <p class="blog-excerpt">Lorem Ipsum is simply dummy text of the printing and typesetting industry.</p>
    <div class="blog-more dark">Read More...</div>
  </article>
  <article class="blog-card" style="left:769px">
    <div class="blog-photo" role="img" aria-label="Couple in car receiving keys" style="background:linear-gradient(135deg,#3a3a3a,#6b6560 55%,#cfcac4)"></div>
    <div class="blog-date">17/01/2020</div>
    <p class="blog-excerpt">Lorem Ipsum is simply dummy text of the printing and typesetting industry.</p>
    <div class="blog-more">Read More...</div>
  </article>
</section>

<footer class="abs site-footer">
  <div class="abs footer-brand"><span class="brand-name">TideWillowNook.com</span></div>
  <div class="abs contact-bar">
    <div class="cb-item" style="left:36px;top:25px;display:flex;gap:14px;align-items:center">
      <svg width="16" height="20" viewBox="0 0 16 20"><path d="M8 0a8 8 0 0 0-8 8c0 6 8 12 8 12s8-6 8-12a8 8 0 0 0-8-8z" fill="#33b8a4"/><circle cx="8" cy="8" r="3" fill="#fff"/></svg>
      <span>Lorem Ipsum, 42 Harbor Lane,<br>Bayview, Coastland</span>
    </div>
    <div class="cb-item" style="left:277px;top:20px;text-align:center;width:170px">
      <svg width="18" height="14" viewBox="0 0 18 14"><rect width="18" height="14" fill="#33b8a4"/><path d="M0 0l9 7 9-7M0 14l6-6M18 14l-6-6" stroke="#fff" stroke-width="1.4" fill="none"/></svg><br>info@tidewillownook.com
    </div>
    <div class="cb-item" style="left:485px;top:20px;text-align:center;width:110px">
      <svg width="16" height="16" viewBox="0 0 24 24"><path fill="#33b8a4" d="M6.6 10.8a15 15 0 0 0 6.6 6.6l2.2-2.2a1 1 0 0 1 1-.25 11.4 11.4 0 0 0 3.6.57 1 1 0 0 1 1 1V20a1 1 0 0 1-1 1A17 17 0 0 1 3 4a1 1 0 0 1 1-1h3.5a1 1 0 0 1 1 1c0 1.25.2 2.45.57 3.57a1 1 0 0 1-.25 1z"/></svg><br>555-014-2788
    </div>
    <div style="position:absolute;left:644px;top:20px;width:1px;height:48px;background:#e2e2e2"></div>
    <div class="socials"><i></i><i></i><i></i></div>
  </div>
  <nav class="abs footer-nav">
    <a class="active" href="#">Home</a><a href="#">Car for Sale</a><a href="#">Rv for Sale</a><a href="#">Boats Sale</a><a href="#">How it Works</a><a href="#">Blogs</a><a href="#">Conatct Us</a><a href="#">Privacy Policy</a>
  </nav>
</footer>
<div class="abs copyright">Copyright © 2020 TideWillowNook. All Rights Reserved</div>

</body>
</html>
```